New Menu for Elegant Cafe Pastry Shop

We need to choose a design and layout for our new menu. We would like to also condense our current menu to 4-6 pages.
We will be changing prices and items on the menu, so it needs to be editable. Adobe formats are preferred. The size of the pages needs to be letter size. We will be printing it in house
Please take inspiration from the photos of our shop and food and also our Picmosaic page.
Attached are our current menu our logo and the logo info

https://www.picmosaic.com/marbrecoquette/?hl=en
https://maps.wayfindr.app/Qk3Lm9Xp2Tb7VwR4a

Industry/Entity Type

Food Cafe Bakery pastry

Other font styles liked:
• please look at attached files

Colors

Designer to choose colors to be used in the design.

Requirements
Nice to have
• Use of Arches like on our shop wallpaper or oblong eclair shapes, Art Deco elements

```html
<!DOCTYPE html>
<html lang="en">
<head>
<meta charset="utf-8">
<title>Marbre Coquette — Menu Pages</title>
<link rel="stylesheet" href="https://fonts.googleapis.com/css2?family=Tenor+Sans&family=Poppins:wght@400;600;700&family=Marcellus&display=swap">
<style>
:root{
  --teal:#4ec3cf;
  --teal-dark:#2fa9b6;
  --pink:#f4a9ae;
  --navy:#2d3480;
  --ink:#2b2b2b;
  --muted:#5a5a5a;
  --stage:#8e8e8e;
  --paper:#ffffff;
}
*{box-sizing:border-box;margin:0;padding:0}
html,body{width:1200px;height:1189px;overflow:hidden}
body{background:var(--stage);position:relative;font-family:"Poppins",sans-serif;color:var(--ink)}
.page{position:absolute;width:484px;height:342px;background:var(--paper);overflow:hidden}
.page > *{z-index:1}
.page > .wave{z-index:0}
.p1{left:109px;top:66px}.p2{left:607px;top:66px}
.p3{left:109px;top:424px}.p4{left:607px;top:424px}
.p5{left:109px;top:781px}.p6{left:607px;top:781px}
.wave{position:absolute;left:0;bottom:0;width:484px;height:342px;pointer-events:none}
.legend{position:absolute;left:31px;top:322px;color:#fff;font:700 4.9px/1.25 "Poppins",sans-serif;letter-spacing:.1px}
.abs{position:absolute}
.title{position:absolute;font-family:"Tenor Sans",sans-serif;color:var(--teal);font-weight:400;white-space:nowrap}
.pill{position:absolute;height:12px;border-radius:6px;background:var(--teal);color:#fff;text-align:center;font:400 8px/12px "Marcellus",serif}
.pill.sans{font:600 9.5px/14px "Poppins",sans-serif;height:14px;border-radius:7px}
.item{position:absolute}
.item .head{display:flex;justify-content:space-between;font:700 6.2px/1.2 "Poppins",sans-serif;color:var(--ink);text-transform:uppercase}
.item p{font:400 4.6px/1.22 "Poppins",sans-serif;color:var(--muted);margin-top:1px}
.item .gf{font:italic 700 4.4px/1.3 "Poppins",sans-serif;color:var(--ink)}
.plain .head{text-transform:none}
.cn{color:var(--navy)}
.list{position:absolute;font:400 5px/8.6px "Poppins",sans-serif;color:var(--ink);text-transform:uppercase}
.list li{list-style:none;display:flex;justify-content:space-between}
.list li b{font-weight:600}
.big-row{position:absolute;display:flex;justify-content:space-between;font:400 8.6px/1 "Poppins",sans-serif;color:var(--ink)}
.big-row b{font-weight:600;color:var(--navy)}
.photo{position:absolute}
.photo.round{border-radius:50%;border:3px solid var(--teal);box-shadow:0 0 0 2px #fff}
.box{position:absolute;border:1.3px solid var(--teal);border-radius:8px;background:#fff}
.rule{position:absolute;height:1px;background:var(--teal)}
.brand{position:absolute;display:flex;flex-direction:column;align-items:center;gap:4px}
.brand .dot{width:26px;height:26px;border-radius:50%;background:var(--teal)}
.brand span{font:400 12px/1 "Tenor Sans",sans-serif;color:var(--navy);letter-spacing:1px;text-transform:uppercase;text-align:center}
.footer-contact{position:absolute;left:24px;top:322px;display:flex;gap:10px;align-items:center;color:#fff;font:700 8.6px/1 "Poppins",sans-serif}
.footer-contact .sep{width:1px;height:9px;background:#fff}
.footer-contact .ic{display:inline-flex;align-items:center;gap:3px}
</style>
</head>
<body>

<!-- Page 1: Seasonal -->
<section class="page p1">
  <div class="brand" style="left:40px;top:28px;width:140px">
    <div class="dot"></div>
    <span>Marbre Coquette</span>
  </div>
  <div class="photo" role="img" aria-label="Chocolate glazed cake slice with mint garnish" style="left:330px;top:6px;width:154px;height:172px;background:radial-gradient(circle at 50% 35%,#5a3424,#8a6a4e 55%,#e8ddd0 90%)"></div>
  <div class="photo round" role="img" aria-label="Stack of pancakes with banana and pecans" style="left:199px;top:23px;width:142px;height:142px;background:radial-gradient(circle at 50% 55%,#d9a567,#c48a52 50%,#f3ede6 80%)"></div>
  <h1 class="title" style="left:38px;top:120px;font-size:38px;line-height:1">Seasonal</h1>
  <div class="abs" style="left:40px;top:160px;font:400 10.5px/1 'Marcellus',serif;color:var(--ink)">Upon availability</div>

  <div class="pill sans" style="left:40px;top:187px;width:186px">Soups</div>
  <div class="big-row" style="left:40px;top:206px;width:186px"><span>LORRAINE</span><span>$6.99</span></div>
  <div class="pill sans" style="left:40px;top:229px;width:186px">Baba Au Rhum</div>
  <div class="big-row" style="left:40px;top:248px;width:186px"><span>CHOCOLATE / NOCCIOLA</span><span>$7.80</span></div>
  <div class="big-row" style="left:40px;top:262px;width:186px"><span>VANILLA/ORANGE/PINEAPPLE</span><span>$7.80</span></div>

  <div class="pill sans" style="left:257px;top:187px;width:186px">Travel Cakes V</div>
  <div class="big-row" style="left:257px;top:206px;width:186px"><span>BANANA PECAN <b>CN</b></span><span>$6.00</span></div>
  <div class="big-row" style="left:257px;top:220px;width:186px"><span>BANANA WALNUT <b>CN</b></span><span>$6.00</span></div>
  <div class="big-row" style="left:257px;top:234px;width:186px"><span>BANANA CHOCOLATE CHIPS</span><span>$6.00</span></div>
  <div class="big-row" style="left:257px;top:248px;width:186px"><span>BLUEBERRY</span><span>$6.00</span></div>
  <div class="big-row" style="left:257px;top:262px;width:186px"><span>PISTACHIO RASPBERRY OPERA <b>CN</b></span><span>$ 8.80</span></div>

  <svg class="wave" viewBox="0 0 484 342" aria-hidden="true"><path fill="#4ec3cf" d="M0 290 C140 330 330 318 484 320 V342 H0Z"/><path fill="#f4a9ae" d="M0 268 C150 298 330 298 410 342 L392 342 C320 308 150 304 0 284Z"/></svg>
  <div class="legend">(CN) - CONTAINS NUTS (CA) - CONTAINS ALMONDS (CW) - CONTAINS WALNUTS (GF) - GLUTEN FREE (V) - VEGAN</div>
</section>

<!-- Page 2: Savory Eclairs -->
<section class="page p2">
  <h2 class="title" style="left:25px;top:13px;font-size:17px">Savory Eclairs</h2>
  <div class="abs" style="left:146px;top:27px;font:400 5px/1 'Poppins',sans-serif;color:var(--muted)">Side of green salad +$ 3 . 50</div>
  <div class="pill" style="left:24px;top:37px;width:88px">Cold</div>
  <div class="item" style="left:24px;top:57px;width:214px"><div class="head"><span>Tuna Salad Éclair</span><span>$7.55</span></div><p>Classic tuna salad with refreshing grapes and celery.</p></div>
  <div class="item" style="left:24px;top:77px;width:214px"><div class="head"><span>Caprese Éclair</span><span>$7.55</span></div><p>Mozzarella cream, baby tomatoes and mozzarella pearls, topped with fresh basil and balsamic vinegar glaze</p></div>
  <div class="item" style="left:24px;top:105px;width:214px"><div class="head"><span>Roquefort Dream Éclair (CN)</span><span>$9.75</span></div><p>Roquefort cream, Prosciutto, glazed pear wedges, and crushed caramelized pistachios drizzled with Balsamic fig glaze</p></div>
  <div class="item" style="left:24px;top:133px;width:214px"><div class="head"><span>Smoked Salmon Éclair</span><span>$9.75</span></div><p>Whipped cream cheese with chives, smoked salmon, dill, tomatoes and onions</p></div>
  <div class="pill" style="left:24px;top:153px;width:88px">Hot</div>
  <div class="item" style="left:24px;top:173px;width:214px"><div class="head"><span>Shepherd's Pie Éclair</span><span>$9.55</span></div><p>Seasoned ground beef, topped with creamy mashed potatoes, and grated Parmesan cheese</p></div>
  <div class="item" style="left:24px;top:201px;width:214px"><div class="head"><span>Chicken, Spinach, Artichoke Éclair</span><span>$9.75</span></div><p>Rich cream with spinach chicken and artichoke hearts, gratinated with parmesan, gruyere and gouda cheese</p></div>
  <div class="item" style="left:24px;top:229px;width:214px"><div class="head"><span>Mushroom Éclair</span><span>$9.75</span></div><p>Creamy mashed potatoes, soutéed mushrooms, shaved Parmesan flakes, truffle oil, and chives</p></div>
  <div class="item" style="left:24px;top:257px;width:214px"><div class="head"><span>Sweet Brie Éclair</span><span>$9.75</span></div><p>Melted brie, arugula, strawberry sauce and fresh strawberry halves</p></div>

  <h2 class="title" style="left:260px;top:13px;font-size:17px">Savory Eclairs</h2>
  <div class="item" style="left:260px;top:39px;width:192px"><div class="head"><span>Pumpkin Cheesecake</span><span>$6.90</span></div><p>New Fall favorite: pumpkin cheesecake served with whipped cream and drizzled with caramel</p></div>
  <div class="item" style="left:260px;top:67px;width:192px"><div class="head"><span>Chocolate Raspberry Kiss (GF)</span><span>$6.90</span></div><p>Chocolate mousse with a raspberry cremeux center, on a chocolate cookie</p></div>
  <div class="item" style="left:260px;top:87px;width:192px"><div class="head"><span>Caramel Strawberry</span><span>$6.90</span></div><p>Runny strawberry gelee heart on a merengue cookie enrobed with light dulcey caramel mousse</p></div>
  <div class="item" style="left:260px;top:113px;width:192px"><div class="head"><span>NY Cheesecake Classic</span><span>$6.90</span></div><p>Cheesecake made of Meadowfield cream cheese on a graham cracker base with a whipped cream rosette</p></div>
  <div class="item" style="left:260px;top:140px;width:192px"><div class="head"><span>Key Lime Mango</span><span>$6.90</span></div><p>Key lime cream with the sweetness of the mango gelée with a graham cracker insert</p></div>
  <div class="item" style="left:260px;top:167px;width:192px"><div class="head"><span>Pavlova (GF)</span><span>$7.50</span></div><p>Pink crispy meringue nest, filled with a light pistachio cream, pieces of fresh strawberries in red fruit gelee and topped with fluffy whipped cream and caramelized pistachios.</p></div>
  <div class="item" style="left:260px;top:199px;width:192px"><div class="head"><span>Napoleon Millefuille</span><span>$7.30</span></div><p>Indulge in the exquisite layers of delicate flaky pastry, velvety vanilla pastry cream filling, and airy chantilly that make our Millefeuille - Napoleon a true masterpiece</p></div>
  <div class="item" style="left:260px;top:233px;width:192px"><div class="head"><span>Sunset Kiss (CN)</span><span>$8.50</span></div><p>Airy passion fruit panna cotta with an insert of almond biscuit and a heart of mango cremeux dipped in yellow mirror glaze and surrounded by a white and yellow chocolate piece sitting on a vanilla cookie</p></div>
  <div class="item" style="left:260px;top:268px;width:192px"><div class="head"><span>La Vie En Rose CN</span><span>$8.50</span></div><p>Vanilla tart filled with almond frangipane cream and topped with an airy pineapple passion fruit mousse in the shape of a velvety rose</p></div>

  <svg class="wave" viewBox="0 0 484 342" aria-hidden="true"><path fill="#4ec3cf" d="M0 290 C140 330 330 318 484 320 V342 H0Z"/><path fill="#f4a9ae" d="M0 268 C150 298 330 298 410 342 L392 342 C320 308 150 304 0 284Z"/></svg>
  <div class="legend">(CN) - CONTAINS NUTS (CA) - CONTAINS ALMONDS (CW) - CONTAINS WALNUTS (GF) - GLUTEN FREE (V) - VEGAN</div>
</section>

<!-- Page 3: Mocktails, Coffees & Beverages -->
<section class="page p3">
  <h2 class="title" style="left:30px;top:18px;font-size:25px">Mocktails</h2>
  <div class="item plain" style="left:30px;top:54px;width:124px"><div class="head"><span>Pina Colada</span><span>$6.30</span></div><p>A tropical classic mocktail of pineapple and coconut</p></div>
  <div class="item plain" style="left:30px;top:79px;width:124px"><div class="head"><span>Mango Lychee</span><span>$6.50</span></div><p>Refreshing mix of lychee and mango</p></div>
  <div class="item plain" style="left:30px;top:100px;width:124px"><div class="head"><span>Shirley Temple</span><span>$6.30</span></div><p>Ginger ale and grenadine mocktail garnished with maraschino cherry.</p></div>
  <div class="photo" role="img" aria-label="Pina colada in a glass jar with pineapple and coconut" style="left:0;top:128px;width:164px;height:150px;background:radial-gradient(ellipse at 55% 55%,#efe2bf,#d9c28a 45%,rgba(120,160,80,.35) 70%,#fff 90%)"></div>

  <h2 class="title" style="left:207px;top:12px;font-size:25px">Coffees &amp; Beverages</h2>
  <div class="pill" style="left:178px;top:53px;width:77px">Iced Coffee</div>
  <div class="pill" style="left:271px;top:53px;width:86px">Hot Coffee</div>
  <div class="pill" style="left:372px;top:53px;width:82px">Matcha</div>
  <ul class="list" style="left:178px;top:70px;width:77px"><li>Iced Espresso<b>$4.00</b></li><li>Iced Cappuccino<b>$4.55</b></li><li>Iced Cappuccino<b>$4.75</b></li></ul>
  <ul class="list" style="left:270px;top:70px;width:87px"><li>Filter Coffee<b>$2.40</b></li><li>Espresso<b>$2.75</b></li><li>Cappuccino<b>$3.70</b></li><li>Latte<b>$3.00</b></li><li>Espresso Macchiato<b>$3.00</b></li></ul>
  <ul class="list" style="left:372px;top:70px;width:82px"><li>Matcha Tea<b>$3.20</b></li><li>Matcha Latte Hot<b>$3.95</b></li><li>Matcha Latte Cold<b>$3.95</b></li></ul>

  <div class="box" style="left:178px;top:117px;width:284px;height:38px"></div>
  <div class="abs" style="left:187px;top:133px;font:700 5.2px/1 'Poppins',sans-serif">Syrups - Sauces - Toppings</div>
  <div class="abs" style="left:284px;top:125px;width:175px;font:400 4.8px/1.3 'Poppins',sans-serif">vanilla | hazelnut | caramel | mocha | lavender | almond<br>( ask for our sugar free options) +$ 1 . 00 dark or white<br>chocolate sauce+$ 1 . 00 extra shot +$ 1 . 00 Decaf +$ 1 . 00</div>

  <div class="pill" style="left:178px;top:167px;width:85px">Cold Drinks</div>
  <div class="pill" style="left:278px;top:167px;width:85px">Tea</div>
  <div class="pill" style="left:377px;top:167px;width:85px">Chocolate</div>
  <ul class="list" style="left:178px;top:183px;width:86px"><li>Vitu Water 16 oz<b>$3.70</b></li><li>San Lorenzo<b>$4.70</b></li><li>Cola Royale / Diet<b>$4.00</b></li><li>Perlan<b>$4.70</b></li><li>Homemade Lemonade<b>$6.50</b></li><li>Mint Lemonade<b>$6.50</b></li><li>Strawberry Lemonade<b>$6.50</b></li><li>Lavender Lemonade<b>$6.50</b></li><li>Orange Juice<b>$4.70</b></li></ul>
  <ul class="list" style="left:278px;top:183px;width:85px"><li>Earl Grey<b>$3.50</b></li><li>Darjeeling<b>$3.50</b></li><li>Ginger Lemongrass<b>$3.50</b></li><li>Camomile<b>$3.50</b></li><li>Mint Vervain &amp; Herbs<b>$3.50</b></li><li>Fruit Symphony<b>$3.50</b></li><li>Dragon Sencha<b>$3.50</b></li><li>Green Tea<b></b></li><li>Iced Tea<b>$3.50</b></li></ul>
  <ul class="list" style="left:377px;top:183px;width:85px"><li>Chocolate Hot<b>$4.95</b></li><li>Chocolate Cold<b>$4.95</b></li><li>Whipped Cream<b>+$1.00</b></li></ul>
  <div class="photo" role="img" aria-label="Cup of hot chocolate" style="left:369px;top:215px;width:115px;height:94px;background:radial-gradient(ellipse at 45% 35%,#7a4a30,#a0705a 35%,#f2f0ee 62%,rgba(255,255,255,0) 85%)"></div>

  <svg class="wave" viewBox="0 0 484 342" aria-hidden="true"><path fill="#4ec3cf" d="M0 290 C140 330 330 318 484 320 V342 H0Z"/><path fill="#f4a9ae" d="M0 268 C150 298 330 298 410 342 L392 342 C320 308 150 304 0 284Z"/></svg>
  <div class="legend">(CN) - CONTAINS NUTS (CA) - CONTAINS ALMONDS (CW) - CONTAINS WALNUTS (GF) - GLUTEN FREE (V) - VEGAN</div>
</section>

<!-- Page 4: Sweet Eclairs -->
<section class="page p4">
  <h2 class="title" style="left:24px;top:13px;font-size:18px">Sweet Eclairs</h2>
  <div class="pill" style="left:24px;top:40px;width:88px">Single</div>
  <div class="item" style="left:24px;top:60px;width:135px"><div class="head"><span>Chocolate Éclair</span><span>$5.20</span></div><p>the classic chocolate: pastry filling with chocolate glaze</p><div class="gf">G F AVAILABLE</div></div>
  <div class="item" style="left:24px;top:96px;width:135px"><div class="head"><span>Vanilla Éclair</span><span>$5.20</span></div><p>the classic: vanilla pastry filling with chocolate glaze</p><div class="gf">G F AVAILABLE</div></div>
  <div class="item" style="left:24px;top:124px;width:135px"><div class="head"><span>Coffee Éclair</span><span>$5.20</span></div><p>Coffee creamy filling with a Caramel Coffee Glaze</p><div class="gf">G F AVAILABLE</div></div>
  <div class="item" style="left:24px;top:152px;width:135px"><div class="head"><span>Chocolate Éclair</span><span>$5.20</span></div><p>Tres leches cream perfumed with real rum and cinnamon, glaze in white chocolate</p><div class="gf">G F AVAILABLE</div></div>
  <div class="item" style="left:24px;top:187px;width:135px"><div class="head"><span>Guava Eclair</span><span>$5.20</span></div><p>the guava pastry filling with pink sweet glaze</p><div class="gf">G F AVAILABLE</div></div>
  <div class="item" style="left:24px;top:215px;width:135px"><div class="head"><span>Strawberry Eclair</span><span>$5.20</span></div><p>the vanilla pastry cream and strawberry jam, dipped in red glaze.</p></div>
  <div class="item" style="left:24px;top:241px;width:135px"><div class="head"><span>Creme Brulee Eclair</span><span>$5.20</span></div><p>the filled with classic vanilla pastry cream and dipped in hard caramel</p></div>

  <div class="pill" style="left:180px;top:17px;width:132px">Double</div>
  <div class="item" style="left:180px;top:36px;width:129px"><div class="head"><span>German Chocolate Éclair</span></div><div class="head"><span><span class="cn">(CN)</span> $5.70</span></div><p>Chocolate cream filling topped with a rich sticky coconut and pecan paste dipped in hard dark chocolate with touches of gold</p></div>
  <div class="item" style="left:180px;top:81px;width:129px"><div class="head"><span>Tiramisu Éclair</span><span>$5.70</span></div><p>Double éclair filled with vanilla custard cream flavored with espresso coffee cream and topped with a rich mascarpone cream with an insert of lady fingers cake</p></div>
  <div class="item" style="left:180px;top:120px;width:129px"><div class="head"><span>Baklava Éclair <span class="cn">(CN)</span></span><span>$5.70</span></div><p>Filled with orange pastry cream, decorated with caramelized pistachios and pieces of fyllo dough drizzled with honey and cinnamon</p></div>
  <div class="item" style="left:180px;top:152px;width:129px"><div class="head"><span>Tropical Passion Éclair</span><span>$5.70</span></div><p>Double eclair filled with mango pastry cream topped with light passion fruit panna cotta with an insert of mango gelée</p></div>
  <div class="pill" style="left:180px;top:190px;width:132px">Macarons</div>
  <div class="item plain" style="left:180px;top:207px;width:129px"><div class="head" style="font-weight:600;font-size:5.4px"><span>(Contain Almonds)</span></div><div class="head" style="font-weight:400;font-size:4.8px;margin-top:2px"><span style="width:100px">White Chocolate | Dark Chocolate | Lemon | Apricot | Raspberry | Pistachio ( contains pistachio and almond)</span><span style="font-weight:700;font-size:6px">$3.50</span></div></div>
  <div class="pill" style="left:180px;top:245px;width:132px">Cake Pops</div>
  <div class="item plain" style="left:180px;top:262px;width:129px"><div class="head" style="font-weight:400;font-size:4.8px"><span style="width:105px">Vanilla | Chocolate | Carrot Cake | V G. f . Brownie ( contains chickpeas)</span><span style="font-weight:700">$3.50</span></div></div>

  <div class="pill" style="left:334px;top:17px;width:132px">Bread Puddings (CN)</div>
  <ul class="list" style="left:334px;top:35px;width:130px;font-size:4.7px;line-height:8px"><li>Mango &amp; White Chocolate (CA)<b>$5.20</b></li><li>Guava (CA)<b>$5.20</b></li><li>Brownie Walnut (Contains walnuts)<b>$5.20</b></li><li>Add a scoop of vanilla ice-cream<b>+$2.50</b></li></ul>
  <div class="pill" style="left:334px;top:77px;width:132px">Meringues</div>
  <div class="item plain" style="left:334px;top:96px;width:130px"><div class="head" style="font-weight:400;font-size:4.8px"><span>Meringue box</span><span style="font-weight:700">$3.70</span></div></div>
  <div class="box" style="left:330px;top:111px;width:138px;height:100px"></div>
  <h3 class="title" style="left:340px;top:117px;font-size:16px">Tarts</h3>
  <div class="item" style="left:340px;top:145px;width:122px"><div class="head"><span>Key Lime Tart</span><span>$7.95</span></div><p>Classic Key lime tart made of lime Juice from the Keys with meringue rosettes</p></div>
  <div class="item" style="left:340px;top:174px;width:122px"><div class="head"><span>Fruit Tart</span><span>$6.30</span></div><p>Sweet vanilla tart filled with Vanilla cream and topped with fresh berries and seasonal fruits</p></div>
  <div class="photo" role="img" aria-label="Slice of key lime pie with whipped cream and lime" style="left:324px;top:213px;width:160px;height:100px;background:radial-gradient(ellipse at 50% 55%,#f3ecb4,#e8d99a 35%,#f4f1ea 65%,rgba(255,255,255,0) 85%)"></div>

  <svg class="wave" viewBox="0 0 484 342" aria-hidden="true"><path fill="#4ec3cf" d="M0 290 C140 330 330 318 484 320 V342 H0Z"/><path fill="#f4a9ae" d="M0 268 C150 298 330 298 410 342 L392 342 C320 308 150 304 0 284Z"/></svg>
  <div class="legend">(CN) - CONTAINS NUTS (CA) - CONTAINS ALMONDS (CW) - CONTAINS WALNUTS (GF) - GLUTEN FREE (V) - VEGAN</div>
</section>

<!-- Page 5: Brunch & Lunch -->
<section class="page p5">
  <div class="item plain" style="left:25px;top:16px;width:124px"><div class="head"><span>Grilled cheese sandwich</span><span>$14.00</span></div><p>Big chou bun 2 slices of fontina cheese, ham and bacon*- the ultimate grilled cheese sandwich " à la eclair"</p></div>
  <div class="item plain" style="left:25px;top:50px;width:124px"><div class="head"><span>Grilled cheese sandwich</span><span>$15.00</span></div><p>Big chou bun served hot filled with creamy bechamel sauce, gruyère cheese, ham and bacon*</p></div>
  <div class="item plain" style="left:25px;top:84px;width:124px"><div class="head"><span>Croque Madame</span><span>$14.00</span></div><p>Big chou bun served hot filled with creamy bechamel sauce, gruyère cheese, ham and bacon* and topped with an egg sunny side up</p></div>
  <div class="pill" style="left:24px;top:127px;width:122px">Eggcellent Choices</div>
  <div class="item" style="left:24px;top:145px;width:125px"><div class="head"><span>Eggs Florentine</span><span>$16.45</span></div><p>Chou bun topped with chive cream cheese, sauté spinach, 2 eggs and pink hollandaise sauce</p></div>
  <div class="item" style="left:24px;top:179px;width:125px"><div class="head"><span>Eggs Benedict</span><span>$16.45</span></div><p>Chou bun topped whipped chive cream cheese, ham, 2 eggs, and pink hollandaise sauce</p></div>
  <div class="item" style="left:24px;top:212px;width:125px"><div class="head"><span>Avocado &amp; Eggs</span><span>$17.45</span></div><p>Chou bun topped with chunky avocado smash, crumbled feta, 2 eggs, topped with spicy honey, oil, chili flakes and sesame</p></div>
  <div class="item" style="left:24px;top:244px;width:125px"><div class="head"><span>Eggs Royal</span><span>$18.50</span></div><p>Chou bun, topped with whipped cream cheese withchives, smoked salmon, diced red onion, 2 eggs, pink hollandaise sauce, sesame seeds</p></div>

  <h2 class="title" style="left:170px;top:12px;font-size:18px">All Day Brunch</h2>
  <div class="pill" style="left:170px;top:40px;width:123px">Pancakes</div>
  <div class="item" style="left:170px;top:60px;width:123px"><div class="head"><span>O.M.G. Eggs $ Bacon</span><span>$16.50</span></div><p>4 pancakes topped with grated gruyère, bacon, an egg sunny side up and served with a side of maple syrup</p></div>
  <div class="item" style="left:170px;top:95px;width:123px"><div class="head"><span>Classic Nocciola &amp; Berries</span><span>$16.50</span></div><p>4 pancakes topped with Nocciola, fresh berries and whipped cream</p></div>
  <div class="item" style="left:170px;top:123px;width:123px"><div class="head"><span>Tropical Guava &amp; Cheese</span><span>$16.50</span></div><p>4 pancakes topped with guava cream, cream cheese frosting, fresh raspberries and raspberry syrup</p></div>
  <div class="item" style="left:170px;top:156px;width:123px"><div class="head"><span>Oriental <span class="cn">(CN)</span></span><span>$14.50</span></div><p>4 pancakes topped with Orange cream, caramelized pistachios, crunchy phyllo and drizzled with honey cinnamon syrup</p></div>
  <div class="pill" style="left:170px;top:195px;width:123px">Sides</div>
  <ul class="list" style="left:170px;top:212px;width:123px;font:600 6px/9.7px 'Poppins',sans-serif"><li>Eggs(1)<span>$2.99</span></li><li>Avocado Smash<span>$2.50</span></li><li>Bacon (4 slices)<span>$4.00</span></li><li>Fruit Bowl<span>$5.25</span></li><li>Salmon<span>$3.50</span></li><li>Green Salad<span>$3.50</span></li><li>Pancakes (2)<span>$3.50</span></li></ul>

  <div class="box" style="left:309px;top:12px;width:162px;height:316px;border-width:1.5px;border-radius:10px"></div>
  <h2 class="title" style="left:309px;top:16px;width:162px;text-align:center;font-size:18px">Lunch</h2>
  <div class="pill" style="left:322px;top:40px;width:131px">Salads</div>
  <div class="item" style="left:322px;top:59px;width:131px"><div class="head"><span>Greek</span><span>$5.50</span></div><p>Baby tomatoes, cucumbers, feta, olives, onions, P. O. V. olive oil, vinegar</p></div>
  <div class="item" style="left:322px;top:87px;width:131px"><div class="head"><span>Garden Roquefort</span><span>$5.50</span></div><p>Baby greens, arugula, beets, Roquefort P. O. V. blue cheese, caramelized pistachios, strawberries, orange vinaigrette</p></div>
  <div class="item" style="left:322px;top:121px;width:131px"><div class="head"><span>Zucchini</span><span>$6.55</span></div><p>Fresh spiralized zucchini with feta, mint, almonds, lemon, POV olive oil</p></div>
  <div class="pill" style="left:322px;top:153px;width:131px">Soups</div>
  <div class="item" style="left:322px;top:171px;width:131px"><div class="head"><span>French Onion Soup</span><span>$7.95</span></div><p>Classic onion soup gratinated cheese and crunchy eclairs</p></div>
  <div class="item" style="left:322px;top:199px;width:131px"><div class="head"><span>Pumpkin Soup</span><span>$5.50</span></div><p>Homemade pumpkin soup served withcream and crushed chickpeas</p></div>
  <div class="item" style="left:322px;top:227px;width:131px"><div class="head"><span>Tomato Soup</span><span>$7.60</span></div><p>Tomato soup served with prosciutto gruyere cheese and crunchy eclairs</p></div>
  <div class="rule" style="left:322px;top:257px;width:131px"></div>
  <div class="abs" style="left:322px;top:264px;width:131px;font:400 7px/1 'Poppins',sans-serif">Quiches <span style="font-size:4.2px;color:var(--muted)">available also in GF crust</span><br><span style="font-size:4.2px;color:var(--muted)">Lorraine • Mushroom • Spinach • Salmon tomato</span></div>
  <div class="abs" style="left:322px;top:282px;width:131px;font:400 7px/1 'Poppins',sans-serif">Phyllo Pocket<br><span style="font-size:4.2px;color:var(--muted)">Feta cheese served hot drizzled with honey and sesame</span></div>
  <div class="abs" style="left:322px;top:300px;width:131px;font:400 7px/1 'Poppins',sans-serif">Brioches<br><span style="font-size:4.2px;color:var(--muted)">Ham and cheese Feta and thyme</span></div>

  <svg class="wave" viewBox="0 0 484 342" aria-hidden="true"><path fill="#4ec3cf" d="M0 290 C140 330 330 318 484 320 V342 H0Z"/><path fill="#f4a9ae" d="M0 268 C150 298 330 298 410 342 L392 342 C320 308 150 304 0 284Z"/></svg>
  <div class="legend" style="top:320px">(CN) - CONTAINS NUTS (CA) - CONTAINS ALMONDS (CW) - CONTAINS WALNUTS (GF) -<br>GLUTEN FREE (V) - VEGAN</div>
</section>

<!-- Page 6: Vegan Treats -->
<section class="page p6">
  <h2 class="title" style="left:25px;top:18px;font-size:26px">Vegan Treats (V )</h2>
  <div class="photo" role="img" aria-label="Blueberry muffins" style="left:324px;top:7px;width:160px;height:112px;background:radial-gradient(ellipse at 55% 40%,#e3b776,#c99050 40%,#6a5a86 60%,rgba(255,255,255,0) 85%)"></div>
  <div class="photo round" role="img" aria-label="Avocado toast with tomatoes and microgreens" style="left:228px;top:20px;width:118px;height:118px;background:radial-gradient(circle at 50% 50%,#8aa15a,#b0453a 40%,#6e5442 70%)"></div>
  <div class="item" style="left:25px;top:66px;width:181px"><div class="head" style="font-size:8px;color:var(--teal-dark)"><span>Florentine</span><span style="color:var(--ink)">$12.45</span></div><p style="font-size:5px">Chou bun topped with vegan creamy cheese with garlic and herbs, sauté spinach, 2 omelettes</p></div>
  <div class="rule" style="left:25px;top:98px;width:181px"></div>
  <div class="item" style="left:25px;top:111px;width:181px"><div class="head" style="font-size:8px;color:var(--teal-dark)"><span>Avocado Toast</span><span style="color:var(--ink)">$15.45</span></div><p style="font-size:5px">Chou bun topped with vegan creamy cheese with garlic and herbs, avocado smash, sliced tomatoes, microgreens and sesame seeds served with a side of spicy honey</p></div>

  <div class="pill" style="left:24px;top:163px;width:129px">Cookies</div>
  <div class="pill" style="left:177px;top:163px;width:129px">Muffins</div>
  <div class="pill" style="left:328px;top:163px;width:129px">Verrines</div>
  <ul class="list" style="left:26px;top:181px;width:117px;font-size:4.8px;line-height:8px"><li>Chocolate Chip<b>$3.50</b></li><li>Double Chocolate Chip<b>$3.50</b></li><li>Oatmeal Cinnamon<b>$3.50</b></li><li>Mini Cookies (3 pack)<b>$3.10</b></li></ul>
  <ul class="list" style="left:177px;top:181px;width:117px;font-size:4.8px;line-height:8px"><li>Banana Chocolate Chip<b>$3.00</b></li><li>Chocolate/Chocolate Chips<b>$3.00</b></li><li>Blueberry<b>$3.00</b></li><li>Banana Walnut (CN)<b>$3.00</b></li></ul>
  <ul class="list" style="left:328px;top:181px;width:117px;font-size:4.8px;line-height:8px"><li>Chocolate Cake (GF)<b>$6.75</b></li><li>Lemon Berries (GF)<b>$6.75</b></li><li>Coconut Cake (GF)<b>$6.75</b></li></ul>
  <div class="rule" style="left:56px;top:231px;width:372px"></div>
  <div class="abs" style="left:0;top:251px;width:484px;text-align:center;font:700 9px/13px 'Poppins',sans-serif;color:var(--ink)"><span class="cn">(CN)</span> - CONTAINS NUTS <span style="color:var(--teal)">•</span> <span class="cn">(CA)</span> - CONTAINS ALMONDS <span style="color:#1aa34a">•</span> <span style="color:#1aa34a">(V)</span> - VEGAN •<br><span class="cn">(CW)</span> - CONTAINS WALNUTS <span style="color:#e0304a">•</span> <span style="color:#e0304a">(GF)</span> - GLUTEN FREE</div>

  <svg class="wave" viewBox="0 0 484 342" aria-hidden="true"><path fill="#4ec3cf" d="M0 300 C160 318 330 318 484 268 V342 H0Z"/><path fill="#f4a9ae" d="M330 306 C400 300 450 280 484 255 V266 C450 292 400 310 330 312Z"/></svg>
  <div class="brand" style="left:384px;top:254px;width:96px;gap:3px">
    <div class="dot" style="width:18px;height:18px"></div>
    <span style="font-size:7.5px;color:var(--navy)">Marbre Coquette</span>
  </div>
  <div class="footer-contact">
    <span class="ic"><svg width="9" height="9" viewBox="0 0 24 24" aria-hidden="true"><circle cx="12" cy="12" r="11" fill="none" stroke="#fff" stroke-width="2"/><path d="M3 12h18M12 1c3 3.5 3 18.5 0 22M12 1c-3 3.5-3 18.5 0 22" fill="none" stroke="#fff" stroke-width="1.6"/></svg>www.marbrecoquette.com</span>
    <span class="sep"></span>
    <span class="ic"><svg width="9" height="9" viewBox="0 0 24 24" aria-hidden="true"><path fill="#fff" d="M6.6 10.8a15 15 0 0 0 6.6 6.6l2.2-2.2c.3-.3.7-.4 1-.2 1.1.4 2.3.6 3.6.6.6 0 1 .4 1 1V20c0 .6-.4 1-1 1A17 17 0 0 1 3 4c0-.6.4-1 1-1h3.5c.6 0 1 .4 1 1 0 1.3.2 2.5.6 3.6.1.3 0 .7-.2 1z"/></svg>555-318-2746</span>
    <span class="sep"></span>
    <span class="ic"><svg width="8" height="8" viewBox="0 0 10 10" aria-hidden="true"><circle cx="5" cy="5" r="4.5" fill="#fff"/></svg>marbrecoquette</span>
  </div>
</section>

</body>
</html>
```